need corporate, modern business card created for Consulting Company

I need a slick business card using elements from my website, as well as, integrating my pixelharbor-created logo (see files).

The business card needs to be:
1. Corporate and modern
2. Clean and professional

I've included a PSD with the logo/icon that you can use to create it. Feel free to try a metallic finish on the logo, make it bigger/small, underlay it. Whatever you need to do to make my card stand out.

Try a black background, or white background or gray.

The idea is for my card to be memorable as well as professional and corporate.

Target Market(s)

Corporate business in the US and Canada.

Industry/Entity Type

Business

Contact Information for Business Card

Business Leveraging Technology
Malcolm Tudd, Senior Partner
office: 1 877 555 0143
mobile: 1 519 555 0172
website: http://www.vextorial.com

Requirements
Must have
• Card-related information
• corporate, yet modern
• clean and professional
• incorporate the icon only
• must have an editable form when complete!
Nice to have
• metallic icon might be cool
• try it with white or black

```html
<!DOCTYPE html>
<html lang="en">
<head>
<meta charset="utf-8">
<title>Vextorial – Business Card</title>
<link rel="stylesheet" href="https://fonts.googleapis.com/css2?family=Comfortaa:wght@400;700&family=Oswald:wght@400;500&display=swap">
<style>
  :root {
    --stage: #161616;
    --card-dark: #121212;
    --card-mid: #2c2c2c;
    --ink-white: #f2f2f2;
    --ink-soft: #c9ccd2;
    --brand-blue: #3d72c4;
    --band-blue: #3e6399;
    --band-blue-light: #5b82bb;
  }
  * { box-sizing: border-box; margin: 0; padding: 0; }
  html, body {
    width: 1200px; height: 871px; overflow: hidden;
    background: var(--stage);
  }
  .stage { position: relative; width: 1200px; height: 871px; }

  .card {
    position: absolute;
    border-radius: 4px;
    overflow: hidden;
    box-shadow: 0 18px 40px rgba(0,0,0,.6);
  }

  /* Back of card */
  .card-back {
    left: 90px; top: 70px; width: 560px; height: 320px;
    background: linear-gradient(160deg, #1e1e1e 0%, #050505 55%, #000 100%);
  }
  .card-back .band {
    position: absolute; left: 0; right: 0; bottom: 0; height: 92px;
    background: linear-gradient(90deg, var(--band-blue-light), var(--band-blue));
    display: flex; align-items: center; justify-content: space-between;
    padding: 0 34px;
  }
  .card-back .band-url {
    font-family: "Oswald", sans-serif; font-weight: 500;
    font-size: 18px; letter-spacing: 3px; color: var(--ink-soft);
  }
  .card-back .wordmark { color: var(--ink-white); font-size: 32px; }

  /* Front of card */
  .card-front {
    left: 550px; top: 440px; width: 600px; height: 343px;
    background: linear-gradient(150deg, #3a3a3a 0%, var(--card-mid) 30%, #1a1a1a 65%, var(--card-dark) 100%);
  }
  .accent-bar {
    position: absolute; left: 44px; top: 0; width: 6px; height: 148px;
    background: var(--brand-blue);
  }
  .identity { position: absolute; left: 74px; top: 44px; }
  .identity .name {
    font-family: "Comfortaa", sans-serif; font-weight: 400;
    font-size: 31px; color: var(--ink-white); letter-spacing: .5px;
  }
  .identity .title {
    margin-top: 4px;
    font-family: "Oswald", sans-serif; font-weight: 400;
    font-size: 12px; letter-spacing: 2.5px; color: var(--brand-blue);
  }

  .brand { position: absolute; right: 40px; top: 92px; display: flex; align-items: center; gap: 12px; }
  .brand-square { width: 34px; height: 34px; background: var(--brand-blue); }
  .wordmark {
    font-family: "Comfortaa", sans-serif; font-weight: 700;
    font-size: 44px; color: var(--brand-blue); letter-spacing: .5px;
  }

  .contacts {
    position: absolute; left: 40px; top: 196px; list-style: none;
    font-family: "Oswald", sans-serif; font-weight: 400;
    font-size: 18px; letter-spacing: 2.4px; color: var(--ink-white);
  }
  .contacts li { display: flex; align-items: center; gap: 14px; height: 28px; }
  .contacts svg { width: 16px; height: 16px; fill: var(--ink-soft); flex: none; }

  .web {
    position: absolute; right: 46px; bottom: 34px;
    display: flex; align-items: center; gap: 14px;
    font-family: "Oswald", sans-serif; font-weight: 500;
    font-size: 18px; letter-spacing: 3px; color: var(--brand-blue);
  }
  .web svg { width: 18px; height: 18px; }
</style>
</head>
<body>
<main class="stage">

  <section class="card card-back" aria-label="Card back">
    <div class="band">
      <span class="band-url">www.vextorial.com</span>
      <span class="wordmark">vextorial</span>
    </div>
  </section>

  <section class="card card-front" aria-label="Card front">
    <div class="accent-bar"></div>
    <div class="identity">
      <h1 class="name">Malcolm Tudd</h1>
      <p class="title">Senior Partner</p>
    </div>

    <div class="brand">
      <span class="brand-square"></span>
      <span class="wordmark">vextorial</span>
    </div>

    <ul class="contacts">
      <li>
        <svg viewBox="0 0 16 16" aria-hidden="true"><path d="M2 5c0-2 2-3 6-3s6 1 6 3v1h-3V5H5v1H2zM4 7h8l2 6H2z"/></svg>
        <span>1 877 555 0143</span>
      </li>
      <li>
        <svg viewBox="0 0 16 16" aria-hidden="true"><path d="M4 1h8v14H4zM5.5 3v9h5V3z"/></svg>
        <span>1 519 555 0172</span>
      </li>
      <li>
        <svg viewBox="0 0 16 16" aria-hidden="true"><path d="M1 4h14v9H1zM2 5l6 4 6-4v-.2H2z"/></svg>
        <span>info@vextorial.com</span>
      </li>
    </ul>

    <div class="web">
      <svg viewBox="0 0 18 18" aria-hidden="true"><circle cx="9" cy="9" r="8" fill="#3d72c4"/><path d="M1 9h16M9 1c3 3 3 13 0 16M9 1c-3 3-3 13 0 16" stroke="#1a1a1a" stroke-width="1.3" fill="none"/></svg>
      <span>www.vextorial.com</span>
    </div>
  </section>

</main>
</body>
</html>
```